Website-Design für die neue Handtaschenmarke Marvona
Zielgruppe
Frauen und auch Männer, die ästhetisch ausgearbeitete und gleichzeitig zweckmäßige Handtaschen und Accessoires suchen. Frauen, die Einzelstücke nach ihren Wünschen und Bedürfnissen angefertigt haben wollen.
Aufgabenstellung
Es soll die Startseite für eine Website mit einem kleinen angebundenen Online-Shop entstehen.
Es gibt keine bestehende Website, nur das Logo steht fest.
Das detailierte Briefing finden Sie als PDF Dokument in der Anlage.

```html
<!DOCTYPE html>
<html lang="de">
<head>
<meta charset="utf-8">
<title>Marvona – Handtaschen</title>
<link rel="stylesheet" href="https://fonts.googleapis.com/css2?family=Arimo:wght@400;700&display=swap">
<style>
  :root {
    --page: #ffffff;
    --ink: #111111;
    --rule: #9a9a9a;
    --frame: #8c8c8c;
    --leather: #4f3530;
    --denim: #4a73b4;
  }
  * { box-sizing: border-box; margin: 0; padding: 0; }
  html, body {
    width: 1200px; height: 848px; overflow: hidden;
    background: var(--page);
    font-family: "Arimo", Arial, sans-serif;
    color: var(--ink);
  }
  .site {
    position: absolute; left: 44px; top: 20px;
    width: 1112px; height: 758px;
    border: 1.5px solid var(--frame);
  }
  .util {
    position: absolute; top: 20px;
    border-top: 1.5px solid var(--rule);
    padding-top: 4px;
    font-size: 12px; font-weight: 700;
  }
  .util--cart { left: 40px; width: 226px; }
  .util--login { left: 270px; width: 256px; }
  .brand {
    position: absolute; right: 64px; top: 26px;
    font-size: 30px; letter-spacing: 1.5px; font-weight: 400;
    text-align: right;
  }
  .main-nav {
    position: absolute; top: 126px; left: 40px;
    font-size: 16px; letter-spacing: 0.3px;
  }
  .main-nav a { position: absolute; white-space: nowrap; color: var(--ink); text-decoration: none; }
  .panel {
    position: absolute; top: 188px; height: 476px;
    border: 1.5px solid var(--frame);
  }
  .panel--categories { left: 44px; width: 224px; padding: 12px 12px; font-size: 15px; line-height: 19px; }
  .panel--categories ul { list-style: none; margin-top: 19px; }
  .panel--categories .sale { margin-top: 19px; }
  .panel--details { left: 278px; width: 266px; padding: 12px 14px; font-size: 12px; line-height: 15px; }
  .product-name { font-weight: 700; margin-bottom: 14px; }
  .product-desc { margin-bottom: 14px; }
  .panel__cart {
    position: absolute; left: 16px; right: 16px; top: 434px;
    border-top: 1.5px solid var(--rule);
    padding-top: 4px; font-size: 12px; font-weight: 700;
  }
  .panel--gallery { left: 556px; width: 506px; }
  .product-image {
    position: absolute; left: 42px; top: 54px; width: 432px; height: 340px;
    background: linear-gradient(180deg, var(--denim) 0%, var(--leather) 100%);
  }
  .gallery-nav {
    position: absolute; left: 46px; top: 440px;
    font-size: 13px; word-spacing: 2px;
  }
  .gallery-nav span { margin-left: 10px; }
  .site-mark {
    position: absolute; left: 42px; top: 700px;
    font-size: 16px;
  }
  .footer-nav {
    position: absolute; left: 44px; top: 788px; width: 1112px;
    font-size: 16px;
  }
  .footer-nav a { position: absolute; color: var(--ink); text-decoration: none; white-space: nowrap; }
</style>
</head>
<body>
  <div class="site">
    <div class="util util--cart">Warenkorb</div>
    <div class="util util--login">Login</div>
    <div class="brand">MARVONA</div>

    <nav class="main-nav">
      <a href="#" style="left:0">UNTERNEHMEN</a>
      <a href="#" style="left:158px">PRODUKTE</a>
      <a href="#" style="left:278px">NEUHEITEN</a>
      <a href="#" style="left:404px">SERVICE</a>
      <a href="#" style="left:506px">KONTAKT</a>
    </nav>

    <aside class="panel panel--categories">
      <div>PRODUKTE</div>
      <ul>
        <li>DAMEN</li>
        <li>HERREN</li>
        <li>HERBST 2010</li>
        <li>NEUHEITEN</li>
      </ul>
      <div class="sale">SALE</div>
    </aside>

    <section class="panel panel--details">
      <div class="product-name">SELVA</div>
      <p class="product-desc">Das zeigt sich in Design und Ästhetik unserer Taschen. Dafür Garantieren wir.</p>
      <p>Material: Leder<br>Technik: Smok<br>Maße: 35 x 35 x 10 cm</p>
      <div class="panel__cart">Warenkorb</div>
    </section>

    <section class="panel panel--gallery">
      <div class="product-image" role="img" aria-label="Produktfoto: braune Ledertasche mit blauem Smok-Einsatz und geflochtenen blauen Henkeln"></div>
      <div class="gallery-nav">1 2 3 4 <span>ZOOM</span></div>
    </section>

    <div class="site-mark">Marvona</div>
  </div>

  <nav class="footer-nav">
    <a href="#" style="left:40px">IMPRESSUM</a>
    <a href="#" style="left:168px">AGB</a>
    <a href="#" style="left:234px">BLOG</a>
    <a href="#" style="left:310px">KREISNETZ</a>
  </nav>
</body>
</html>
```